I need to rebrand my public user portal for a new/modern look and feel

I want to take my current user web portal and redesign the look of it. I have included 2 samples of my current user portal and would like options to create a new functional look. This main page below will modify based on the tabs on the top left. Any questions please ask.

```html
<!DOCTYPE html>
<html lang="en">
<head>
<meta charset="utf-8">
<title>Student Portal Dashboard – Two Header Styles</title>
<link href="https://fonts.googleapis.com/css2?family=Noto+Sans:wght@400;500;600;700&display=swap" rel="stylesheet">
<style>
:root{
  --stage:#7a7a7a;
  --gold:#8b7941;
  --gold-soft:#f3efe4;
  --gold-line:#c9bd98;
  --brand-red:#9b2a2f;
  --alert-red:#d8262c;
  --up-green:#2f9a4a;
  --ink:#1f1f1f;
  --muted:#8a8a8a;
  --line:#ececf0;
  --card:#ffffff;
  --page-a:#f7f4f6;
  --page-b:#f8f8fc;
}
*{box-sizing:border-box;margin:0;padding:0}
html,body{width:1200px;height:1200px;overflow:hidden}
body{background:var(--stage);font-family:"Noto Sans",sans-serif;color:var(--ink);position:relative}
.screen{position:absolute;left:166px;width:1398px;height:857px;transform:scale(.6211);transform-origin:0 0;overflow:hidden}
.screen--gold{top:45px;background:linear-gradient(180deg,var(--page-a) 0%,#f5f1f3 70%,#f3e9ed 100%)}
.screen--light{top:623px;background:var(--page-b)}
.topbar{position:absolute;left:0;top:0;width:100%;height:65px;display:flex;align-items:center}
.screen--gold .topbar{background:var(--gold);border-bottom:3px solid var(--brand-red);color:#fff}
.screen--light .topbar{background:#fff;border-bottom:1px solid var(--line)}
.brand{position:absolute;left:40px;top:20px;display:flex;align-items:center;gap:8px;font-size:15px;font-weight:600}
.brand-mark{width:16px;height:16px;background:currentColor}
.screen--gold .brand{color:#f2ecdc}
.screen--light .brand{color:var(--brand-red)}
.nav{position:absolute;left:368px;top:0;height:62px;display:flex;align-items:center;gap:34px;font-size:15px}
.nav-item{display:flex;align-items:center;gap:9px}
.nav-item svg{width:18px;height:18px}
.screen--gold .nav-item--active{font-weight:600}
.screen--light .nav-item--active{color:var(--brand-red);font-weight:500}
.user{position:absolute;right:44px;top:12px;display:flex;align-items:center;gap:14px;font-size:13px;font-weight:700}
.avatar{width:38px;height:38px;border-radius:50%;background:radial-gradient(circle at 50% 40%,#c9a68a 0 35%,#5a6f7a 36%);border:2px solid #fff}
.screen--light .avatar{border-color:#d9d3c3}
.user svg{width:14px;height:14px}
.stat-card{position:absolute;top:127px;width:416px;height:152px;background:var(--card);border-radius:8px;box-shadow:0 2px 10px rgba(0,0,0,.06)}
.stat-title{position:absolute;left:32px;top:19px;font-size:17px;font-weight:500}
.stat-range{position:absolute;right:20px;top:20px;font-size:12px;font-weight:500;display:flex;align-items:center;gap:10px}
.stat-range svg{width:12px;height:12px;color:var(--gold)}
.stat-total{position:absolute;left:32px;top:54px;font-size:38px;font-weight:400}
.stat-label{position:absolute;top:108px;font-size:14px;color:var(--muted)}
.stat-move{position:absolute;top:84px;font-size:16px;display:flex;align-items:center;gap:4px}
.stat-move svg{width:14px;height:14px}
.move-in svg{color:var(--up-green)}
.move-out svg{color:var(--alert-red)}
.tabs{position:absolute;left:66px;top:328px;display:flex;gap:24px;font-size:16px;color:#777}
.tab{padding-bottom:17px;position:relative}
.tab--active{color:var(--brand-red);font-weight:500}
.tab--active::after{content:"";position:absolute;left:0;right:0;bottom:0;height:3px;background:var(--brand-red)}
.roster{position:absolute;left:42px;top:375px;width:1314px;height:439px;background:#fff;border-radius:6px;box-shadow:0 1px 6px rgba(0,0,0,.04)}
.roster-head{height:82px;border-bottom:1px solid var(--line);position:relative}
.roster-brand{position:absolute;left:48px;top:30px;display:flex;align-items:center;gap:7px;font-size:14px;font-weight:600;color:var(--brand-red)}
.roster-brand .brand-mark{width:13px;height:13px}
.roster-title{position:absolute;left:160px;top:26px;font-size:22px;font-weight:500}
.roster-divider{position:absolute;left:421px;top:25px;width:1px;height:32px;background:#ddd}
.add-btn{position:absolute;left:445px;top:23px;width:171px;height:36px;border:1px solid var(--gold-line);background:var(--gold-soft);border-radius:3px;font-size:15px;font-weight:500;display:flex;align-items:center;justify-content:center;gap:14px}
.add-btn svg{width:12px;height:12px}
.filter-btn{position:absolute;left:1247px;top:21px;width:35px;height:34px;border:1px solid var(--gold-line);background:var(--gold-soft);border-radius:3px;display:flex;align-items:center;justify-content:center;color:var(--gold)}
.filter-btn svg{width:17px;height:17px}
.col-head,.row{position:relative;border-bottom:1px solid var(--line)}
.col-head{height:51px;font-size:15px;font-weight:600}
.row{height:61px;font-size:15px}
.row:last-child{border-bottom:none}
.cell{position:absolute;top:50%;transform:translateY(-50%)}
.c-name{left:48px;display:flex;align-items:center;gap:13px}
.c-grade{left:393px}
.c-year{left:625px;display:flex;align-items:center;gap:12px}
.c-year svg{width:12px;height:12px;color:var(--gold)}
.c-school{left:871px}
.row .c-grade{margin-top:-3px}
.row .c-year,.row .c-school{margin-top:3px}
.expander{width:19px;height:19px;border-radius:50%;background:#e9e9ec;display:flex;align-items:center;justify-content:center}
.expander svg{width:8px;height:8px;color:#777}
.actions{position:absolute;left:1112px;top:13px;display:flex;gap:9px}
.act{width:51px;height:33px;border:1px solid var(--gold-line);background:var(--gold-soft);border-radius:3px;display:flex;align-items:center;justify-content:center;color:var(--gold)}
.act svg{width:17px;height:17px}
.act--delete{color:var(--alert-red)}
</style>
</head>
<body>

<svg width="0" height="0" style="position:absolute">
  <defs>
    <symbol id="i-home" viewBox="0 0 24 24" fill="none" stroke="currentColor" stroke-width="2" stroke-linejoin="round"><path d="M4 10l8-6 8 6v10H4z"/><path d="M10 20v-5h4v5"/></symbol>
    <symbol id="i-layers" viewBox="0 0 24 24" fill="none" stroke="currentColor" stroke-width="2" stroke-linejoin="round"><path d="M12 3l9 5-9 5-9-5z"/><path d="M3 12l9 5 9-5"/><path d="M3 16l9 5 9-5"/></symbol>
    <symbol id="i-file" viewBox="0 0 24 24" fill="none" stroke="currentColor" stroke-width="2" stroke-linejoin="round"><path d="M6 3h8l4 4v14H6z"/><path d="M14 3v4h4"/></symbol>
    <symbol id="i-userplus" viewBox="0 0 24 24" fill="none" stroke="currentColor" stroke-width="2" stroke-linecap="round"><circle cx="9" cy="8" r="4"/><path d="M2 20c1-4 4-6 7-6s6 2 7 6"/><path d="M19 8v6M16 11h6"/></symbol>
    <symbol id="i-chev" viewBox="0 0 24 24" fill="none" stroke="currentColor" stroke-width="3" stroke-linecap="round" stroke-linejoin="round"><path d="M5 9l7 7 7-7"/></symbol>
    <symbol id="i-down" viewBox="0 0 24 24" fill="none" stroke="currentColor" stroke-width="3" stroke-linecap="round" stroke-linejoin="round"><path d="M12 3v18M5 14l7 7 7-7"/></symbol>
    <symbol id="i-up" viewBox="0 0 24 24" fill="none" stroke="currentColor" stroke-width="3" stroke-linecap="round" stroke-linejoin="round"><path d="M12 21V3M5 10l7-7 7 7"/></symbol>
    <symbol id="i-filter" viewBox="0 0 24 24" fill="none" stroke="currentColor" stroke-width="1.8" stroke-linejoin="round"><path d="M3 4h18l-7 9v6l-4 2v-8z"/></symbol>
    <symbol id="i-pen" viewBox="0 0 24 24" fill="none" stroke="currentColor" stroke-width="1.8" stroke-linejoin="round"><path d="M4 20l1-5L16 4l4 4L9 19z"/><path d="M4 20h16"/></symbol>
    <symbol id="i-eye" viewBox="0 0 24 24" fill="none" stroke="currentColor" stroke-width="1.8"><path d="M2 12s4-6 10-6 10 6 10 6-4 6-10 6S2 12 2 12z"/><circle cx="12" cy="12" r="3"/></symbol>
    <symbol id="i-trash" viewBox="0 0 24 24" fill="none" stroke="currentColor" stroke-width="2" stroke-linejoin="round"><path d="M4 6h16M9 6V3h6v3M6 6l1 15h10l1-15M10 10v7M14 10v7"/></symbol>
    <symbol id="i-play" viewBox="0 0 10 10"><path d="M3 1l5 4-5 4z" fill="currentColor"/></symbol>
  </defs>
</svg>

<!-- Gold header variant -->
<section class="screen screen--gold">
  <header class="topbar">
    <div class="brand"><span class="brand-mark"></span>Meridian Works</div>
    <nav class="nav">
      <span class="nav-item nav-item--active"><svg><use href="#i-home"/></svg>Dashboard</span>
      <span class="nav-item"><svg><use href="#i-layers"/></svg>Applications</span>
      <span class="nav-item"><svg><use href="#i-file"/></svg>Transcript Request</span>
      <span class="nav-item"><svg><use href="#i-userplus"/></svg>New Hire Packet</span>
    </nav>
    <div class="user">Hi, Dana.m<div class="avatar" role="img" aria-label="User profile photo"></div><svg><use href="#i-chev"/></svg></div>
  </header>

  <article class="stat-card" style="left:42px">
    <h3 class="stat-title">GradeLedgerDemo</h3>
    <div class="stat-range">Last 7 Days<svg><use href="#i-chev"/></svg></div>
    <div class="stat-total">100</div>
    <div class="stat-label" style="left:32px">Total Students</div>
    <div class="stat-move move-in" style="left:222px"><svg><use href="#i-down"/></svg>4</div>
    <div class="stat-label" style="left:222px">In - Last7D</div>
    <div class="stat-move move-out" style="left:314px"><svg><use href="#i-up"/></svg>1</div>
    <div class="stat-label" style="left:314px">Out - Last7D</div>
  </article>
  <article class="stat-card" style="left:491px">
    <h3 class="stat-title">KRVTS</h3>
    <div class="stat-range">Last 7 Days<svg><use href="#i-chev"/></svg></div>
    <div class="stat-total">0</div>
    <div class="stat-label" style="left:32px">Total Students</div>
    <div class="stat-move move-in" style="left:222px"><svg><use href="#i-down"/></svg>0</div>
    <div class="stat-label" style="left:222px">In - Last7D</div>
    <div class="stat-move move-out" style="left:314px"><svg><use href="#i-up"/></svg>0</div>
    <div class="stat-label" style="left:314px">Out - Last7D</div>
  </article>
  <article class="stat-card" style="left:940px">
    <h3 class="stat-title">MWSDEMO19</h3>
    <div class="stat-range">Last 7 Days<svg><use href="#i-chev"/></svg></div>
    <div class="stat-total">0</div>
    <div class="stat-label" style="left:32px">Total Students</div>
    <div class="stat-move move-in" style="left:222px"><svg><use href="#i-down"/></svg>0</div>
    <div class="stat-label" style="left:222px">In - Last7D</div>
    <div class="stat-move move-out" style="left:314px"><svg><use href="#i-up"/></svg>0</div>
    <div class="stat-label" style="left:314px">Out - Last7D</div>
  </article>

  <div class="tabs">
    <span class="tab tab--active">GradeLedgerDemo</span>
    <span class="tab">KRVTS</span>
    <span class="tab">MWSDEMO19</span>
  </div>

  <div class="roster">
    <div class="roster-head">
      <div class="roster-brand"><span class="brand-mark"></span>Meridian</div>
      <h2 class="roster-title">GradeLedgerDemo</h2>
      <span class="roster-divider"></span>
      <div class="add-btn">Add Student Via<svg><use href="#i-chev"/></svg></div>
      <div class="filter-btn"><svg><use href="#i-filter"/></svg></div>
    </div>
    <div class="col-head">
      <span class="cell c-name">Name</span><span class="cell c-grade">Grade</span>
      <span class="cell c-year">Year<svg><use href="#i-chev"/></svg></span><span class="cell c-school">School/Building</span>
    </div>
    <div class="row"><span class="cell c-name"><span class="expander"><svg><use href="#i-play"/></svg></span>MWVIEW4210 Testing</span><span class="cell c-grade">KG</span><span class="cell c-year">2024</span><span class="cell c-school">Testing</span>
      <div class="actions"><span class="act"><svg><use href="#i-pen"/></svg></span><span class="act"><svg><use href="#i-eye"/></svg></span><span class="act act--delete"><svg><use href="#i-trash"/></svg></span></div></div>
    <div class="row"><span class="cell c-name"><span class="expander"><svg><use href="#i-play"/></svg></span>dana morrow</span><span class="cell c-grade">KG</span><span class="cell c-year">2024</span><span class="cell c-school">Testing</span>
      <div class="actions"><span class="act"><svg><use href="#i-pen"/></svg></span><span class="act"><svg><use href="#i-eye"/></svg></span><span class="act act--delete"><svg><use href="#i-trash"/></svg></span></div></div>
    <div class="row"><span class="cell c-name"><span class="expander"><svg><use href="#i-play"/></svg></span>dana morrow</span><span class="cell c-grade">KG</span><span class="cell c-year">2024</span><span class="cell c-school">Testing</span>
      <div class="actions"><span class="act"><svg><use href="#i-pen"/></svg></span><span class="act"><svg><use href="#i-eye"/></svg></span><span class="act act--delete"><svg><use href="#i-trash"/></svg></span></div></div>
    <div class="row"><span class="cell c-name"><span class="expander"><svg><use href="#i-play"/></svg></span>dana morrow</span><span class="cell c-grade">KG</span><span class="cell c-year">2024</span><span class="cell c-school">Testing</span>
      <div class="actions"><span class="act"><svg><use href="#i-pen"/></svg></span><span class="act"><svg><use href="#i-eye"/></svg></span><span class="act act--delete"><svg><use href="#i-trash"/></svg></span></div></div>
    <div class="row"><span class="cell c-name"><span class="expander"><svg><use href="#i-play"/></svg></span>dana morrow</span><span class="cell c-grade">KG</span><span class="cell c-year">2024</span><span class="cell c-school">Testing</span>
      <div class="actions"><span class="act"><svg><use href="#i-pen"/></svg></span><span class="act"><svg><use href="#i-eye"/></svg></span><span class="act act--delete"><svg><use href="#i-trash"/></svg></span></div></div>
  </div>
</section>

<!-- Light header variant -->
<section class="screen screen--light">
  <header class="topbar">
    <div class="brand"><span class="brand-mark"></span>Meridian Works</div>
    <nav class="nav">
      <span class="nav-item nav-item--active"><svg><use href="#i-home"/></svg>Dashboard</span>
      <span class="nav-item"><svg><use href="#i-layers"/></svg>Applications</span>
      <span class="nav-item"><svg><use href="#i-file"/></svg>Transcript Request</span>
      <span class="nav-item"><svg><use href="#i-userplus"/></svg>New Hire Packet</span>
    </nav>
    <div class="user">Hi, Dana.m<div class="avatar" role="img" aria-label="User profile photo"></div><svg><use href="#i-chev"/></svg></div>
  </header>

  <article class="stat-card" style="left:42px">
    <h3 class="stat-title">GradeLedgerDemo</h3>
    <div class="stat-range">Last 7 Days<svg><use href="#i-chev"/></svg></div>
    <div class="stat-total">100</div>
    <div class="stat-label" style="left:32px">Total Students</div>
    <div class="stat-move move-in" style="left:222px"><svg><use href="#i-down"/></svg>4</div>
    <div class="stat-label" style="left:222px">In - Last7D</div>
    <div class="stat-move move-out" style="left:314px"><svg><use href="#i-up"/></svg>1</div>
    <div class="stat-label" style="left:314px">Out - Last7D</div>
  </article>
  <article class="stat-card" style="left:491px">
    <h3 class="stat-title">KRVTS</h3>
    <div class="stat-range">Last 7 Days<svg><use href="#i-chev"/></svg></div>
    <div class="stat-total">0</div>
    <div class="stat-label" style="left:32px">Total Students</div>
    <div class="stat-move move-in" style="left:222px"><svg><use href="#i-down"/></svg>0</div>
    <div class="stat-label" style="left:222px">In - Last7D</div>
    <div class="stat-move move-out" style="left:314px"><svg><use href="#i-up"/></svg>0</div>
    <div class="stat-label" style="left:314px">Out - Last7D</div>
  </article>
  <article class="stat-card" style="left:940px">
    <h3 class="stat-title">MWSDEMO19</h3>
    <div class="stat-range">Last 7 Days<svg><use href="#i-chev"/></svg></div>
    <div class="stat-total">0</div>
    <div class="stat-label" style="left:32px">Total Students</div>
    <div class="stat-move move-in" style="left:222px"><svg><use href="#i-down"/></svg>0</div>
    <div class="stat-label" style="left:222px">In - Last7D</div>
    <div class="stat-move move-out" style="left:314px"><svg><use href="#i-up"/></svg>0</div>
    <div class="stat-label" style="left:314px">Out - Last7D</div>
  </article>

  <div class="tabs">
    <span class="tab tab--active">GradeLedgerDemo</span>
    <span class="tab">KRVTS</span>
    <span class="tab">MWSDEMO19</span>
  </div>

  <div class="roster">
    <div class="roster-head">
      <div class="roster-brand"><span class="brand-mark"></span>Meridian</div>
      <h2 class="roster-title">GradeLedgerDemo</h2>
      <span class="roster-divider"></span>
      <div class="add-btn">Add Student Via<svg><use href="#i-chev"/></svg></div>
      <div class="filter-btn"><svg><use href="#i-filter"/></svg></div>
    </div>
    <div class="col-head">
      <span class="cell c-name">Name</span><span class="cell c-grade">Grade</span>
      <span class="cell c-year">Year<svg><use href="#i-chev"/></svg></span><span class="cell c-school">School/Building</span>
    </div>
    <div class="row"><span class="cell c-name"><span class="expander"><svg><use href="#i-play"/></svg></span>MWVIEW4210 Testing</span><span class="cell c-grade">KG</span><span class="cell c-year">2024</span><span class="cell c-school">Testing</span>
      <div class="actions"><span class="act"><svg><use href="#i-pen"/></svg></span><span class="act"><svg><use href="#i-eye"/></svg></span><span class="act act--delete"><svg><use href="#i-trash"/></svg></span></div></div>
    <div class="row"><span class="cell c-name"><span class="expander"><svg><use href="#i-play"/></svg></span>dana morrow</span><span class="cell c-grade">KG</span><span class="cell c-year">2024</span><span class="cell c-school">Testing</span>
      <div class="actions"><span class="act"><svg><use href="#i-pen"/></svg></span><span class="act"><svg><use href="#i-eye"/></svg></span><span class="act act--delete"><svg><use href="#i-trash"/></svg></span></div></div>
    <div class="row"><span class="cell c-name"><span class="expander"><svg><use href="#i-play"/></svg></span>dana morrow</span><span class="cell c-grade">KG</span><span class="cell c-year">2024</span><span class="cell c-school">Testing</span>
      <div class="actions"><span class="act"><svg><use href="#i-pen"/></svg></span><span class="act"><svg><use href="#i-eye"/></svg></span><span class="act act--delete"><svg><use href="#i-trash"/></svg></span></div></div>
    <div class="row"><span class="cell c-name"><span class="expander"><svg><use href="#i-play"/></svg></span>dana morrow</span><span class="cell c-grade">KG</span><span class="cell c-year">2024</span><span class="cell c-school">Testing</span>
      <div class="actions"><span class="act"><svg><use href="#i-pen"/></svg></span><span class="act"><svg><use href="#i-eye"/></svg></span><span class="act act--delete"><svg><use href="#i-trash"/></svg></span></div></div>
    <div class="row"><span class="cell c-name"><span class="expander"><svg><use href="#i-play"/></svg></span>dana morrow</span><span class="cell c-grade">KG</span><span class="cell c-year">2024</span><span class="cell c-school">Testing</span>
      <div class="actions"><span class="act"><svg><use href="#i-pen"/></svg></span><span class="act"><svg><use href="#i-eye"/></svg></span><span class="act act--delete"><svg><use href="#i-trash"/></svg></span></div></div>
  </div>
</section>

</body>
</html>
```